lotwise hub ad

Lotwise hub advert in Australia's leading business paper.
SIZE: 129*92
Must be bold with logo, website, email address (info@lotwisehub.com.au)

Dot points to include:
- Lotwise Hub is at the forefront of market trends
- Directly targeting the property developers and investors market
- 73% of Agencies have listed multiple properties
- Join Melbourne leading Agencies today.

Australia's ONLY dedicated portal for permit approved development sites for sale.

Include standard lotwise hub colours, be creative but bold and clear.

Refer to attachments for inspiration

Thank you
Updates

Hello, we like this design and would like to choose it however can you please complete the following changes immediately as we need to submit content to the newspaper. Remove all current content: Lotwise Hub is at the forefront.... Directly targeting the ....... 73% of Agencies have....... JOIN Melbourne leading.... info@lotwisehub email on the side AND replace with Australia's ONLY dedicated portal for listing Permit Approved Development sites for sale Directly targeting Property Developers and Investors For more information call (03) 9481 2207 or email info@lotwisehub.com.au Your immediate response would be greatly appreciated. Any issues please email me at dale@lotwisehub.com.au Thank you,

Target Market(s)

Real Estate Agents
Property Develops & Investors

Industry/Entity Type

Real Estate Agent

Font styles to use
Serif
Sans Serif

Requirements
Must have
• Refer Project description
Nice to have

```html
<!DOCTYPE html>
<html lang="en">
<head>
<meta charset="utf-8">
<title>Lotwise Hub – Newspaper Advert</title>
<link rel="stylesheet" href="https://fonts.googleapis.com/css2?family=Nunito+Sans:wght@700;800;900&family=Noto+Serif:wght@400;700&display=swap">
<style>
  :root {
    --ink: #2b2b2b;
    --brand: #be1e5a;
    --frame: #cfcfcf;
    --paper: #ffffff;
    --panel-top: #fdfdfd;
    --panel-bottom: #e9ebeb;
    --art-blue: #6fb9e6;
    --art-red: #c9272d;
    --art-ring: #d6d8d8;
  }
  * { margin: 0; padding: 0; box-sizing: border-box; }
  html, body {
    width: 1200px;
    height: 1064px;
    overflow: hidden;
    background: var(--paper);
  }
  .canvas {
    position: relative;
    width: 1200px;
    height: 1064px;
    background: var(--paper);
  }
  .advert {
    position: absolute;
    left: 38px;
    top: 246px;
    width: 1126px;
    height: 803px;
    border: 1px solid var(--frame);
    background: var(--paper);
    overflow: hidden;
    color: var(--ink);
  }
  .advert__side-panel {
    position: absolute;
    left: 0;
    top: 0;
    width: 393px;
    height: 803px;
    background: linear-gradient(to bottom, var(--paper) 0%, var(--panel-top) 45%, var(--panel-bottom) 100%);
  }
  .brand-square {
    position: absolute;
    left: 110px;
    top: 70px;
    width: 170px;
    height: 170px;
    background: var(--brand);
  }
  .approval-art {
    position: absolute;
    left: 28px;
    top: 508px;
    width: 290px;
    height: 270px;
    border-radius: 12px;
    background: radial-gradient(circle at 62% 40%, var(--art-blue) 0%, #b9d8ea 30%, var(--art-ring) 55%, rgba(233,235,235,0) 75%),
                linear-gradient(135deg, rgba(201,39,45,0.25), rgba(201,39,45,0) 60%);
  }
  .wordmark {
    position: absolute;
    left: 412px;
    top: 128px;
    font-family: "Nunito Sans", sans-serif;
    font-weight: 900;
    font-size: 98px;
    line-height: 1;
    letter-spacing: -1px;
    color: var(--brand);
    white-space: nowrap;
  }
  .selling-points {
    position: absolute;
    left: 413px;
    top: 273px;
    list-style: none;
    font-family: "Noto Serif", serif;
    font-weight: 700;
    font-size: 19.5px;
    line-height: 1;
  }
  .selling-points li { height: 46px; }
  .selling-points li:nth-child(2) { height: 43px; }
  .selling-points .brand-name { color: var(--brand); }
  .call-to-action {
    position: absolute;
    left: 413px;
    top: 438px;
    font-family: "Noto Serif", serif;
    font-weight: 700;
    font-size: 23px;
    line-height: 1;
  }
  .contact-email {
    position: absolute;
    left: 412px;
    top: 474px;
    font-family: "Nunito Sans", sans-serif;
    font-weight: 800;
    font-size: 38px;
    line-height: 1;
  }
  .tagline {
    position: absolute;
    left: 414px;
    top: 566px;
    font-family: "Noto Serif", serif;
    font-weight: 400;
    font-size: 30px;
    line-height: 50px;
    color: #333;
  }
  .website {
    position: absolute;
    left: 410px;
    top: 672px;
    font-family: "Nunito Sans", sans-serif;
    font-weight: 800;
    font-size: 68px;
    line-height: 1;
    letter-spacing: -0.5px;
  }
</style>
</head>
<body>
<main class="canvas">
  <section class="advert">
    <div class="advert__side-panel">
      <div class="brand-square"></div>
      <div class="approval-art" role="img" aria-label="Illustration of a folded site map stamped approved"></div>
    </div>

    <h1 class="wordmark">LOTWISE HUB</h1>

    <ul class="selling-points">
      <li><span class="brand-name">Lotwise Hub</span> is at the forefront of market trends</li>
      <li>Directly targeting the property developers and investors market</li>
      <li>73% of Agencies have listed multiple properties</li>
    </ul>

    <p class="call-to-action">Join Melbourne Leading Agencies Today</p>
    <p class="contact-email">info@lotwisehub.com.au</p>

    <p class="tagline">Australia's ONLY dedicated portal for permit<br>approved development sites for sale.</p>

    <p class="website">lotwisehub.com.au</p>
  </section>
</main>
</body>
</html>
```